Mouse and Rodent Infestation Spray

Need to Design label for 16oz bottle. The image sent has our initial design on it. Need other options.

Industry/Entity Type

Pest Control

Colors

Designer to choose colors to be used in the design.

```html
<!DOCTYPE html>
<html lang="en">
<head>
<meta charset="utf-8">
<title>NESTCLEAR Mouse &amp; Rat Spray Label</title>
<link rel="stylesheet" href="https://fonts.googleapis.com/css2?family=Montserrat:ital,wght@0,600;0,800;1,900&family=Quicksand:wght@500;600&family=Oswald:wght@500&display=swap">
<style>
  :root {
    --backdrop: #9b9b9b;
    --label-black: #000000;
    --label-white: #ffffff;
    --brand-red: #e30b14;
    --deep-red: #3a0004;
    --badge-green: #5aa832;
    --badge-blue: #1b6fc2;
  }
  html, body {
    margin: 0;
    padding: 0;
    width: 800px;
    height: 1200px;
    overflow: hidden;
    background: var(--backdrop);
  }
  .label {
    position: absolute;
    left: 90px;
    top: 40px;
    width: 619px;
    height: 1120px;
    background: var(--label-black);
    color: var(--label-white);
    font-family: "Quicksand", sans-serif;
  }
  .label-bands {
    position: absolute;
    inset: 0;
    width: 619px;
    height: 1120px;
  }
  .brand-name {
    position: absolute;
    top: 42px;
    left: 0;
    width: 100%;
    text-align: center;
    font-family: "Montserrat", sans-serif;
    font-weight: 800;
    font-size: 72px;
    letter-spacing: 10px;
    line-height: 1;
    color: var(--label-white);
  }
  .pest-art {
    position: absolute;
    left: 14px;
    top: 206px;
    width: 592px;
    height: 380px;
    background: var(--label-white);
    border-radius: 180px 200px 120px 160px;
  }
  .headline {
    position: absolute;
    left: 100px;
    top: 392px;
    width: 380px;
    text-align: center;
    color: var(--label-black);
  }
  .headline-title {
    margin: 0;
    font-family: "Montserrat", sans-serif;
    font-style: italic;
    font-weight: 900;
    font-size: 46px;
    line-height: 45px;
    letter-spacing: -0.5px;
  }
  .headline-sub {
    margin: 4px 0 0;
    font-family: "Quicksand", sans-serif;
    font-weight: 600;
    font-size: 23px;
  }
  .tagline {
    position: absolute;
    top: 604px;
    left: 0;
    width: 100%;
    text-align: center;
    font-size: 37px;
    font-weight: 500;
  }
  .benefits {
    position: absolute;
    top: 690px;
    left: 0;
    width: 100%;
    text-align: center;
    font-size: 30px;
    font-weight: 500;
    line-height: 54px;
  }
  .benefit {
    display: inline-flex;
    align-items: center;
    margin: 0 6px;
  }
  .tick {
    width: 32px;
    height: 32px;
    margin-right: 6px;
  }
  .safety-badge {
    position: absolute;
    left: 38px;
    top: 895px;
    width: 104px;
    height: 186px;
    border-radius: 8px;
    background: linear-gradient(var(--label-white) 0 40%, var(--badge-blue) 40% 78%, var(--badge-green) 78%);
    border: 4px solid var(--badge-green);
    box-sizing: border-box;
  }
  .natural-claim {
    position: absolute;
    left: 156px;
    top: 940px;
    width: 114px;
    text-align: center;
  }
  .natural-percent {
    font-family: "Oswald", sans-serif;
    font-weight: 500;
    font-size: 58px;
    line-height: 1;
  }
  .natural-word {
    margin-top: 4px;
    background: var(--brand-red);
    color: var(--label-black);
    font-family: "Oswald", sans-serif;
    font-size: 15px;
    letter-spacing: 4px;
    line-height: 18px;
  }
  .natural-product {
    font-family: "Montserrat", sans-serif;
    font-weight: 600;
    font-size: 19px;
    margin-top: 2px;
  }
  .ingredients {
    position: absolute;
    left: 280px;
    top: 888px;
    width: 322px;
    text-align: center;
    font-family: "Montserrat", sans-serif;
    font-weight: 600;
    font-size: 22px;
    line-height: 27px;
    text-transform: uppercase;
  }
  .ingredients p { margin: 0; }
  .percent { color: var(--brand-red); }
  .formula-box {
    position: absolute;
    left: 327px;
    top: 985px;
    width: 292px;
    height: 76px;
    border-radius: 10px 0 0 10px;
    background: linear-gradient(90deg, var(--brand-red) 40%, var(--deep-red));
    display: flex;
    flex-direction: column;
    justify-content: center;
    padding-left: 28px;
    box-sizing: border-box;
    font-family: "Montserrat", sans-serif;
    font-style: italic;
    font-weight: 900;
    font-size: 30px;
    line-height: 31px;
    text-align: left;
  }
  .net-weight {
    position: absolute;
    left: 327px;
    top: 1068px;
    width: 250px;
    text-align: center;
    font-family: "Montserrat", sans-serif;
    font-weight: 600;
    font-size: 27px;
  }
</style>
</head>
<body>
  <main class="label">
    <svg class="label-bands" viewBox="0 0 619 1120" aria-hidden="true">
      <defs>
        <linearGradient id="red-field" x1="0" y1="0" x2="0" y2="1">
          <stop offset="0" stop-color="#e30b14"/>
          <stop offset="0.55" stop-color="#b0060e"/>
          <stop offset="1" stop-color="#3a0004"/>
        </linearGradient>
      </defs>
      <polygon points="0,216 619,140 619,800 0,878" fill="url(#red-field)"/>
      <polygon points="0,204 619,128 619,140 0,216" fill="#ffffff"/>
      <polygon points="0,878 619,800 619,809 0,887" fill="#ffffff"/>
    </svg>

    <div class="brand-name">NESTCLEAR</div>

    <div class="pest-art" role="img" aria-label="White silhouette of a mouse in profile with red ear and whisker details"></div>

    <div class="headline">
      <h1 class="headline-title">MOUSE&amp;RAT<br>INFESTATION</h1>
      <p class="headline-sub">safe for indoor/outdoor use</p>
    </div>

    <div class="tagline">...Safety Guaranteed!</div>

    <div class="benefits">
      <span class="benefit"><svg class="tick" viewBox="0 0 32 32" aria-hidden="true"><rect x="1" y="6" width="24" height="24" fill="#000"/><path d="M6 17 L12 25 L29 2" stroke="#fff" stroke-width="4" fill="none"/></svg>Natural bait</span>
      <span class="benefit"><svg class="tick" viewBox="0 0 32 32" aria-hidden="true"><rect x="1" y="6" width="24" height="24" fill="#000"/><path d="M6 17 L12 25 L29 2" stroke="#fff" stroke-width="4" fill="none"/></svg>Free of pesticides</span><br>
      <span class="benefit"><svg class="tick" viewBox="0 0 32 32" aria-hidden="true"><rect x="1" y="6" width="24" height="24" fill="#000"/><path d="M6 17 L12 25 L29 2" stroke="#fff" stroke-width="4" fill="none"/></svg>Long-lasting control</span>
    </div>

    <div class="safety-badge" role="img" aria-label="Safer product certification badge"></div>

    <div class="natural-claim">
      <div class="natural-percent">100%</div>
      <div class="natural-word">NATURAL</div>
      <div class="natural-product">PRODUCT</div>
    </div>

    <div class="ingredients">
      <p>Active ingredients:</p>
      <p><span class="percent">48%</span> Peppermit oil</p>
      <p><span class="percent">52%</span> Smart ingredients</p>
    </div>

    <div class="formula-box"><span>ADVANCED</span><span>FORMULA</span></div>

    <div class="net-weight">16 OZ</div>
  </main>
</body>
</html>
```